business card design for luxurious real estate brand

using the attached logo, i am looking for a 2-sided business card design. the back should be the gold logo on black background. the front needs to include: gold logo, name, phone, email, and website

Industry/Entity Type

real estate

Contact Information for Business Card

logo, name, email, phone, website

Font styles to use
Sans Serif

```html
<!DOCTYPE html>
<html lang="en">
<head>
<meta charset="utf-8">
<title>Villa Solenne – Business Card</title>
<link href="https://fonts.googleapis.com/css2?family=Montserrat:wght@400;500;600&display=swap" rel="stylesheet">
<style>
  :root {
    --backdrop: #6a6a6a;
    --card: #1a1a1a;
    --gold: #fcd307;
    --ink-light: #f2f2f2;
    --pattern-dark: #141414;
    --pattern-light: #3a3a3a;
  }
  * { box-sizing: border-box; margin: 0; padding: 0; }
  html, body {
    width: 900px; height: 1200px; overflow: hidden;
    background: var(--backdrop);
    font-family: "Montserrat", sans-serif;
  }
  .card {
    position: absolute;
    left: 122px; width: 656px; height: 376px;
    background: var(--card);
    overflow: hidden;
  }
  .card--back { top: 203px; }
  .card--front { top: 620px; }

  .pattern-area {
    position: absolute; inset: 0;
    background: linear-gradient(20deg, var(--pattern-dark) 35%, #262626 65%, var(--pattern-light) 100%);
  }
  .back-mark {
    position: absolute; right: 56px; top: 270px;
    display: flex; align-items: center; gap: 8px;
    color: var(--gold); font-weight: 500; font-size: 14px; letter-spacing: 3px;
    white-space: nowrap;
  }
  .mark-square { width: 14px; height: 14px; background: var(--gold); }

  .contact-block { position: absolute; left: 37px; top: 107px; }
  .person-name {
    color: var(--gold); font-weight: 600; font-size: 26px; letter-spacing: 0.5px; line-height: 1;
  }
  .person-role { color: var(--ink-light); font-size: 15px; margin-top: 6px; letter-spacing: 0.5px; }
  .rule { width: 68px; height: 2px; background: var(--gold); margin: 10px 0 12px; }
  .contact-list { list-style: none; }
  .contact-list li {
    display: flex; align-items: center; gap: 10px;
    color: var(--ink-light); font-size: 14.5px; letter-spacing: 0.8px;
    height: 27.5px; white-space: nowrap;
  }
  .contact-list li.contact-phone { letter-spacing: 2.6px; }
  .contact-list svg { width: 16px; height: 16px; fill: var(--gold); flex: none; }

  .brand-block {
    position: absolute; left: 316px; top: 118px; width: 300px;
    display: flex; flex-direction: column; align-items: center; gap: 28px;
  }
  .brand-square { width: 60px; height: 60px; background: var(--gold); }
  .brand-name {
    color: var(--gold); font-weight: 500; font-size: 26px; letter-spacing: 5px; white-space: nowrap;
  }
</style>
</head>
<body>
  <section class="card card--back">
    <div class="pattern-area" role="img" aria-label="Repeating brand symbol pattern in glossy black and grey tones"></div>
    <div class="back-mark"><span class="mark-square"></span>VILLA SOLENNE</div>
  </section>

  <section class="card card--front">
    <div class="contact-block">
      <h1 class="person-name">DANIEL ROURKE</h1>
      <p class="person-role">Director</p>
      <div class="rule"></div>
      <ul class="contact-list">
        <li class="contact-phone">
          <svg viewBox="0 0 24 24" aria-hidden="true"><path d="M6.6 10.8a15.1 15.1 0 0 0 6.6 6.6l2.2-2.2a1 1 0 0 1 1-.25 11.4 11.4 0 0 0 3.6.57 1 1 0 0 1 1 1V20a1 1 0 0 1-1 1A17 17 0 0 1 3 4a1 1 0 0 1 1-1h3.5a1 1 0 0 1 1 1c0 1.25.2 2.45.57 3.57a1 1 0 0 1-.25 1z"/></svg>
          82-10-4728-3916
        </li>
        <li>
          <svg viewBox="0 0 24 24" aria-hidden="true"><path d="M2 5h20v14H2z M4 7v.5l8 5 8-5V7l-8 5z" fill-rule="evenodd"/></svg>
          info@solennegroup.com
        </li>
        <li>
          <svg viewBox="0 0 24 24" aria-hidden="true"><path d="M12 2a10 10 0 1 0 0 20 10 10 0 0 0 0-20zm0 2c.9 1.2 1.6 2.6 2 4h-4c.4-1.4 1.1-2.8 2-4zM4.3 14a8 8 0 0 1 0-4h3.4a16 16 0 0 0 0 4zm.8 2h3c.3 1.3.8 2.5 1.4 3.6A8 8 0 0 1 5.1 16zM8.1 8h-3a8 8 0 0 1 4.4-3.6C8.9 5.5 8.4 6.7 8.1 8zM12 20c-.9-1.2-1.6-2.6-2-4h4c-.4 1.4-1.1 2.8-2 4zm2.3-6H9.7a14 14 0 0 1 0-4h4.6a14 14 0 0 1 0 4zm.2 5.6c.6-1.1 1.1-2.300 1.4-3.6h3a8 8 0 0 1-4.4 3.6zM16.3 14a16 16 0 0 0 0-4h3.4a8 8 0 0 1 0 4zm-.4-6c-.3-1.3-.8-2.5-1.4-3.6A8 8 0 0 1 18.9 8z"/></svg>
          www.solennegroup.com
        </li>
      </ul>
    </div>
    <div class="brand-block">
      <span class="brand-square"></span>
      <span class="brand-name">VILLA SOLENNE</span>
    </div>
  </section>
</body>
</html>
```